Redesign Of Flower Delivery Subscription Service Website

I need a revamped website of www.petal-rush.com

Please revamp current design using same content....

Target Market(s)

people who buy flowers. Brides, wedding planners, wedding photographer, married man, boyfriend, etc.

Industry/Entity Type

Florist

Number of Pages Required

5+ page

Colors

Designer to choose colors to be used in the design.

Requirements
Must have
• I need a revamped website of www.petal-rush.com
• Please revamp current design using same content....
Nice to have
Should not have

```html
<!DOCTYPE html>
<html lang="en">
<head>
<meta charset="utf-8">
<title>Petal Rush – Monthly Flower Delivery</title>
<link href="https://fonts.googleapis.com/css2?family=Poppins:wght@400;500;600;700&display=swap" rel="stylesheet">
<style>
:root{
  --green:#5da832;
  --green-dark:#3f8a1f;
  --green-light:#8cc63f;
  --mint:#d5efdf;
  --sky:#cfe2ec;
  --ink:#2c2c2c;
  --muted:#555;
  --white:#fff;
}
*{margin:0;padding:0;box-sizing:border-box}
html,body{width:1200px;height:3863px;overflow:hidden;background:var(--white)}
body{font-family:'Poppins',sans-serif;color:var(--ink);position:relative}
.abs{position:absolute}
.hero{left:0;top:0;width:1200px;height:560px;background:linear-gradient(180deg,var(--sky) 0%,#e3eef4 60%,#eef5f8 100%)}
.hero-flowers{right:0;top:0;width:360px;height:520px;background:radial-gradient(circle at 60% 30%,#fff6c8 0%,#ffe066 30%,#f3f6f0 55%,rgba(255,255,255,0) 75%)}
.hero-edge{left:0;top:470px;width:1200px;height:110px}
.brand{left:0;top:28px;width:1200px;text-align:center;font-size:44px;font-weight:500;color:var(--green);letter-spacing:2px;line-height:1}
.brand small{display:block;font-size:13px;color:var(--muted);letter-spacing:1px;margin-top:6px;font-weight:400}
.nav{left:127px;top:136px;display:flex;gap:26px;font-size:15px;font-weight:500;color:var(--ink)}
.hero-title{left:125px;top:208px;font-size:68px;font-weight:400;letter-spacing:2px;line-height:1;color:#333}
.hero-title span{color:var(--green)}
.hero-sub{left:127px;top:305px;font-size:27px;font-weight:600;line-height:1.25;color:#333}
.hero-price{left:127px;top:398px;font-size:29px;font-weight:500;color:#333}
.pill{top:525px;height:42px;border-radius:21px;background:var(--green-light);color:#1f3d0c;font-size:19px;font-weight:700;display:flex;align-items:center;justify-content:center;box-shadow:0 4px 10px rgba(0,0,0,.15)}
.blob{left:0;width:1200px}
.flower-cluster{z-index:0;border-radius:50%;background:radial-gradient(circle at 50% 50%,#f7c6a8 0%,#f3a98a 35%,#7fb069 62%,rgba(255,255,255,0) 70%)}
.section-title{z-index:2;left:0;width:1200px;text-align:center;font-size:27px;font-weight:700;color:var(--green-dark);letter-spacing:1px}
.how-text{z-index:2;left:290px;width:620px;text-align:center;font-size:15.5px;line-height:1.4;color:#333}
.how-text p{margin-bottom:20px}
.video{left:258px;top:1442px;width:687px;height:466px;background:linear-gradient(180deg,#cfcfcf 0%,#f2f2f2 22%,#fafafa 70%,#e9e9e9 86%,#111 86%);box-shadow:0 4px 12px rgba(0,0,0,.3)}
.card-img{top:2052px;width:258px;height:330px;box-shadow:0 3px 10px rgba(0,0,0,.15)}
.card-cap{z-index:2;top:2406px;width:300px;text-align:center;font-size:20px;font-weight:700;color:var(--green-dark);line-height:1.3}
.dots{left:510px;top:2498px}
.news-small{z-index:2;left:0;top:2888px;width:1200px;text-align:center;font-size:22px;font-weight:500;color:#333}
.news-big{z-index:2;left:0;top:2920px;width:1200px;text-align:center;font-size:28px;font-weight:600;color:#333}
.email{z-index:2;left:278px;top:3016px;width:664px;height:64px;border-radius:32px;background:var(--white);box-shadow:0 3px 8px rgba(0,0,0,.15);font-family:Georgia,serif;font-style:italic;font-size:17px;color:#999;padding:22px 0 0 72px}
.subscribe{z-index:2;left:515px;top:3125px;width:168px;height:48px;border-radius:24px;background:var(--green-light);color:var(--white);font-size:20px;font-weight:600;display:flex;align-items:center;justify-content:center}
.footer{left:0;top:3500px;width:1200px;height:363px;background:var(--green)}
.footer-brand{left:0;top:3612px;width:1200px;text-align:center;font-size:52px;font-weight:500;color:var(--white);letter-spacing:2px;line-height:1}
.footer-brand small{display:block;font-size:14px;font-weight:400;letter-spacing:1px;margin-top:8px}
.footer-line{left:0;width:1200px;text-align:center;font-size:16px;color:var(--white);display:flex;justify-content:center;align-items:center;gap:8px}
.copy{left:0;top:3830px;width:1200px;text-align:center;font-size:12px;color:var(--white)}
</style>
</head>
<body>

<header>
  <div class="abs hero"></div>
  <div class="abs hero-flowers" role="img" aria-label="Photo of white daisies and yellow chrysanthemums on pale wood"></div>
  <svg class="abs hero-edge" viewBox="0 0 1200 110" preserveAspectRatio="none" aria-hidden="true">
    <path d="M0 70 C120 90 200 55 320 78 C430 98 520 60 640 82 C760 100 860 40 960 72 C1060 96 1130 60 1200 68 L1200 110 L0 110 Z" fill="#fff"/>
  </svg>
  <div class="abs brand">Petal Rush<small>Coastal Flower Company</small></div>
  <nav class="abs nav"><span>Home</span><span>How it works</span><span>Delivery Areas</span><span>Franchise</span><span>Blog</span><span>Contact</span></nav>
  <h1 class="abs hero-title">PETAL <span>RUSH</span></h1>
  <div class="abs hero-sub">Beautiful Flower Arrangements<br>Delivered Monthly</div>
  <div class="abs hero-price">Now only $69.95/MTH ($100 value)</div>
  <div class="abs pill" style="left:103px;width:162px">FREE VASE</div>
  <div class="abs pill" style="left:301px;width:199px">FREE DELIVERY</div>
  <div class="abs pill" style="left:533px;width:196px">FREE UPGRADE</div>
</header>

<section class="how">
  <svg class="abs blob" style="top:600px;height:820px" viewBox="0 0 1200 820" aria-hidden="true">
    <path d="M300 80 C520 20 760 60 930 30 C1060 10 1150 120 1110 250 C1180 330 1140 430 1050 470 C1080 560 980 640 860 630 C820 720 700 790 580 760 C460 800 360 740 330 650 C240 640 150 580 180 500 C60 470 40 360 130 320 C80 220 170 110 300 80 Z" fill="var(--mint)"/>
  </svg>
  <div class="abs flower-cluster" style="left:228px;top:640px;width:400px;height:290px" role="img" aria-label="Peach gerbera daisies and roses with green leaves"></div>
  <h2 class="abs section-title" style="top:938px">HOW IT WORKS</h2>
  <div class="abs how-text" style="top:995px">
    <p>Petal Rush is a SET IT and FORGET IT subscription based flower delivery service. For an amazing price Petal Rush will hand deliver a gorgeous arrangement directly to anyone, anywhere you want, every month.</p>
    <p>When setting up your account, Petal Rush even lets you choose exact delivery dates for your Anniversary, Birthday, Valentine's and Mother's Day.</p>
    <p>Our referral program is pretty awesome too! Just refer 3 friends and each month your 3 friends pay to have flowers delivered, your flowers will be delivered free!</p>
  </div>
</section>

<section class="abs video" role="img" aria-label="Embedded video: hand sketching a flower vase beside the company name"></section>

<section class="gallery">
  <svg class="abs blob" style="top:2220px;height:440px" viewBox="0 0 1200 440" aria-hidden="true">
    <path d="M0 60 C200 20 420 70 620 30 C820 0 1000 40 1200 20 L1200 330 C1060 360 960 420 800 390 C640 430 520 380 380 410 C240 440 120 380 0 400 Z" fill="var(--mint)"/>
  </svg>
  <div class="abs card-img" style="left:172px;background:linear-gradient(180deg,#6b4b7a,#9a7aa8 50%,#c9b7c6)" role="img" aria-label="Purple roses and lilac arrangement in a glass vase"></div>
  <div class="abs card-img" style="left:494px;background:linear-gradient(180deg,#e8e0c8,#f3ece6 45%,#d9d2c6)" role="img" aria-label="Cream and blush roses in a clear vase"></div>
  <div class="abs card-img" style="left:816px;background:linear-gradient(180deg,#f4f2ef,#d98a85 45%,#6f9a5b 75%,#e9e6e1)" role="img" aria-label="Pink roses with greenery in a red vase"></div>
  <div class="abs card-cap" style="left:151px">SET IT AND FORGET IT</div>
  <div class="abs card-cap" style="left:473px">BUT NEVER FORGET AGAIN</div>
  <div class="abs card-cap" style="left:795px">MAKING SOMEONE'S<br>DAY BETTER</div>
  <svg class="abs dots" width="180" height="14" viewBox="0 0 180 14" aria-hidden="true">
    <line x1="6" y1="7" x2="174" y2="7" stroke="var(--green)" stroke-width="1" stroke-dasharray="2 3"/>
    <circle cx="6" cy="7" r="5" fill="var(--green)"/>
    <circle cx="48" cy="7" r="4" fill="#fff" stroke="var(--green)"/>
    <circle cx="90" cy="7" r="4" fill="#fff" stroke="var(--green)"/>
    <circle cx="132" cy="7" r="4" fill="#fff" stroke="var(--green)"/>
    <circle cx="174" cy="7" r="4" fill="#fff" stroke="var(--green)"/>
  </svg>
  <div class="abs flower-cluster" style="left:935px;top:2475px;width:210px;height:225px;background:radial-gradient(circle at 50% 50%,#e0412c 0%,#f28a5a 30%,#fbe9d2 55%,rgba(255,255,255,0) 70%)" role="img" aria-label="Red carnation with white daisies and a peach rose"></div>
</section>

<section class="newsletter">
  <svg class="abs blob" style="top:2755px;height:670px" viewBox="0 0 1200 670" aria-hidden="true">
    <path d="M420 40 C560 0 700 50 820 20 C930 0 990 90 960 160 C1080 180 1140 260 1080 330 C1120 420 1000 470 880 450 C780 520 620 500 520 470 C380 520 240 470 230 390 C130 370 110 270 190 230 C150 150 260 80 420 40 Z" fill="var(--mint)"/>
  </svg>
  <div class="abs news-small">Enter Your Email To</div>
  <h2 class="abs news-big">Receive A Free Upgrade</h2>
  <div class="abs email">Your email address</div>
  <div class="abs subscribe">SUBSCRIBE</div>
  <div class="abs flower-cluster" style="left:222px;top:3188px;width:280px;height:280px" role="img" aria-label="Peach gerbera daisies and roses with green leaves"></div>
</section>

<footer>
  <svg class="abs" style="left:0;top:3470px" width="1200" height="60" viewBox="0 0 1200 60" preserveAspectRatio="none" aria-hidden="true">
    <path d="M0 40 C150 20 280 45 420 25 C560 8 700 38 860 20 C1000 6 1100 30 1200 18 L1200 60 L0 60 Z" fill="var(--green)"/>
  </svg>
  <div class="abs footer"></div>
  <div class="abs footer-brand">Petal Rush<small>Coastal Flower Company</small></div>
  <div class="abs footer-line" style="top:3737px">
    <svg width="14" height="14" viewBox="0 0 14 14" aria-hidden="true"><path d="M13 1 L1 6 L6 8 L8 13 Z" fill="#fff"/></svg>
    4180 Meadowlark Avenue, Riverton CA 90000
  </div>
  <div class="abs footer-line" style="top:3781px">
    <svg width="16" height="12" viewBox="0 0 16 12" aria-hidden="true"><rect x="0" y="0" width="16" height="12" rx="1" fill="#fff"/><path d="M0 1 L8 7 L16 1" stroke="var(--green)" fill="none"/></svg>
    hello@petal-rush.com
    <svg width="14" height="14" viewBox="0 0 14 14" aria-hidden="true" style="margin-left:6px"><path d="M3 1 L5 1 L6 4 L4.5 5.5 C5.5 7.5 6.5 8.5 8.5 9.5 L10 8 L13 9 L13 11 C13 12 12 13 11 13 C6 13 1 8 1 3 C1 2 2 1 3 1 Z" fill="#fff"/></svg>
    555-204-7718
  </div>
  <div class="abs copy">Copyrights 2018. All Rights are Reserved</div>
</footer>

</body>
</html>
```